Update Business Card Design Project

We've been in business nearly 15 years and about 10 years ago developed a brand that is now well recognized. The business card is boring, too much print and nothing that says 'We are UTTERLY SPLENDID' right off the mark.
We are a fun store, lots of new things on a regular basis. Especially in kitchen goods where the colours are strong and the emphasis is on pretty and practical. We like to have both!
Hi there,
Target Market(s)
Store customers and suppliers
Demographics aged 40-70yrs, mid to high income, mostly women or couples, rural setting but in the 'shopping district' of our region. 1 hour to nearest city.
Industry/Entity Type
Business
Requirements
Nice to have
- Incorporate the logo, if possible

```html
<!DOCTYPE html>
<html lang="en">
<head>
<meta charset="utf-8">
<title>Utterly Splendid – Business Card</title>
<link href="https://fonts.googleapis.com/css2?family=Cinzel:wght@700&family=Arimo:wght@400;700&display=swap" rel="stylesheet">
<style>
  :root {
    --backdrop: #ebe6de;
    --card: #ffffff;
    --ink: #1d1b1b;
    --accent: #f5a20f;
  }
  html, body {
    margin: 0;
    padding: 0;
    overflow: hidden;
  }
  body {
    width: 1157px;
    height: 1200px;
    background: var(--backdrop);
    position: relative;
    font-family: "Arimo", Arial, sans-serif;
    color: var(--ink);
  }
  .card {
    position: absolute;
    background: var(--card);
    border-radius: 20px;
    overflow: hidden;
  }
  .card--front { left: 195px; top: 114px; width: 804px; height: 459px; }
  .card--back  { left: 197px; top: 645px; width: 804px; height: 460px; }

  .brand {
    position: absolute;
    left: 0;
    right: 0;
    text-align: center;
    font-family: "Cinzel", "Times New Roman", serif;
    font-weight: 700;
    color: var(--ink);
  }
  .brand__name {
    display: block;
    letter-spacing: 0.08em;
    white-space: nowrap;
  }
  .brand__tagline {
    display: block;
    letter-spacing: 0.14em;
    white-space: nowrap;
  }
  .card--front .brand { top: 190px; }
  .card--front .brand__name { font-size: 44px; line-height: 56px; }
  .card--front .brand__tagline { font-size: 17px; margin-top: 14px; }

  .card--back .brand { top: 42px; left: 0; width: 808px; }
  .card--back .brand__name { font-size: 25px; line-height: 32px; }
  .card--back .brand__tagline { font-size: 10px; margin-top: 8px; }

  .person {
    position: absolute;
    left: 426px;
    top: 187px;
    width: 378px;
  }
  .person__name {
    width: 426px;
    margin-left: -33px;
    text-align: center;
    font-weight: 700;
    font-size: 17px;
    line-height: 20px;
  }
  .person__rule {
    height: 2px;
    background: var(--accent);
    margin-top: 7px;
  }
  .person__role {
    width: 426px;
    margin-left: -33px;
    text-align: center;
    font-weight: 700;
    font-size: 12px;
    margin-top: 4px;
  }

  .address {
    position: absolute;
    left: 160px;
    top: 234px;
    margin: 0;
    font-style: normal;
    font-size: 14.5px;
    line-height: 22px;
  }
  .contacts {
    position: absolute;
    left: 160px;
    top: 300px;
    margin: 0;
    padding: 0;
    list-style: none;
    font-size: 14.5px;
    line-height: 19px;
  }
  .contacts li {
    display: flex;
    align-items: center;
    gap: 4px;
  }
  .contacts svg { width: 14px; height: 14px; flex: none; }

  .footer-rule {
    position: absolute;
    left: 17px;
    right: 17px;
    top: 392px;
    height: 3px;
    background: var(--accent);
  }
  .footer-band {
    position: absolute;
    left: 17px;
    right: 17px;
    top: 402px;
    height: 20px;
    background: var(--accent);
  }
</style>
</head>
<body>

  <section class="card card--front">
    <div class="brand">
      <span class="brand__name">Utterly Splendid</span>
      <span class="brand__tagline">Bed Bath &amp; Home</span>
    </div>
  </section>

  <section class="card card--back">
    <div class="brand">
      <span class="brand__name">Utterly Splendid</span>
      <span class="brand__tagline">Bed Bath &amp; Home</span>
    </div>

    <div class="person">
      <div class="person__name">Dana Kellis</div>
      <div class="person__rule"></div>
      <div class="person__role">CEO</div>
    </div>

    <address class="address">4-8-12 Minatodai,<br>Sakura-ku, Tokyo 10455</address>

    <ul class="contacts">
      <li>
        <svg viewBox="0 0 14 14" aria-hidden="true"><path d="M4 1.5 C2.5 2.5 2 4.5 2.5 7 C3 9.5 4.5 11.5 6.5 12.5 L8 11 L6.5 9 L5.5 9.5 C4.8 8.5 4.5 6.5 4.8 5 L6 4.6 L5.6 2 Z" fill="var(--accent)"/></svg>
        <span>(021)5550193</span>
      </li>
      <li>
        <svg viewBox="0 0 14 14" aria-hidden="true"><rect x="1.5" y="3" width="11" height="8" fill="none" stroke="var(--accent)" stroke-width="1.3"/><path d="M1.5 3 L7 8 L12.5 3" fill="none" stroke="var(--accent)" stroke-width="1.3"/></svg>
        <span>dana@splendid.com</span>
      </li>
      <li>
        <svg viewBox="0 0 14 14" aria-hidden="true"><circle cx="7" cy="7" r="5" fill="none" stroke="var(--accent)" stroke-width="1.3"/><path d="M2 7 H12 M7 2 C4.8 4.5 4.8 9.5 7 12 M7 2 C9.2 4.5 9.2 9.5 7 12" fill="none" stroke="var(--accent)" stroke-width="1"/></svg>
        <span>www.utterly splendid</span>
      </li>
    </ul>

    <div class="footer-rule"></div>
    <div class="footer-band"></div>
  </section>

</body>
</html>
```